vELRA AirCargo Trailer Wrap

Project: Full exterior livery design for our air cargo road transport trailer., Trailer type: Brevik Ultra Trailer
Base color: White (must remain dominant) About Us VELRA specializes in air freight road transportation. We transport air cargo:
Airport β†’ Logistics hubs
Manufacturers β†’ Airport
We are a last-mile logistics partner in the air cargo industry. A clean, modern, and highly recognizable trailer design that instantly communicates: ✈ Air Cargo πŸš› Road Transport 🌍 International Logistics πŸ”· VELRA brand The design must be minimal but strong.
Professional, premium, and visible from distance.

Design Goals
Clear and bold VELRA logo placement
Strong highway visibility
Aviation-inspired visual elements (subtle, not clichΓ©)
Modern, industrial typography
Clean composition – no clutter
Avoid: overly busy graphics, cartoon airplanes, generic stock icons.
Deliverables
Left side view
Right side view
Rear view

We are looking for a design that makes people immediately think:
β€œAir cargo. Professional. Reliable.”

Target Market(s)

Forwarding

Industry/Entity Type

Transportation

Requirements
Must have
• "LINEHAUL" tag "VELRA logo+ LINEHAUL"
Nice to have
Should not have
• Air cargo/Air freight/Express is boring..

```html
<!DOCTYPE html>
<html lang="hu">
<head>
<meta charset="utf-8">
<title>vELRA Linehaul Trailer Livery</title>
<link rel="stylesheet" href="https://fonts.googleapis.com/css2?family=Montserrat:wght@500;600;700;800&display=swap">
<style>
  :root {
    --navy: #2b3563;
    --red: #e8404b;
    --white: #ffffff;
    --page: #ffffff;
    --frame: #d9dade;
  }
  html, body {
    margin: 0;
    padding: 0;
    width: 874px;
    height: 1200px;
    overflow: hidden;
    background: var(--page);
  }
  .livery {
    display: block;
    width: 874px;
    height: 1200px;
    font-family: "Montserrat", sans-serif;
  }
  .panel-frame { fill: none; stroke: var(--frame); stroke-width: 3; }
  .navy-fill { fill: var(--navy); }
  .white-fill { fill: var(--white); }
  .red-edge { fill: none; stroke: var(--red); stroke-width: 5; stroke-linejoin: miter; }
  .brand-name { font-weight: 800; fill: var(--navy); }
  .brand-dot { fill: var(--red); }
  .linehaul-tag { font-weight: 700; fill: var(--navy); }
  .flight-path { fill: none; stroke-width: 3; stroke-dasharray: 14 10; stroke-linecap: round; }
  .flight-path.on-navy { stroke: var(--red); }
  .flight-path.on-white { stroke: var(--navy); }
  .flight-end { fill: var(--red); }
  .services-title { fill: var(--white); font-weight: 600; font-size: 16px; }
  .service-item { fill: var(--white); font-weight: 600; font-size: 17px; }
  .tick { fill: none; stroke: var(--red); stroke-width: 3; stroke-linecap: round; stroke-linejoin: round; }
  .phone { fill: var(--white); font-weight: 600; font-size: 32px; }
  .web { fill: var(--white); font-weight: 600; font-size: 21px; }
  .tagline { fill: var(--navy); font-weight: 700; font-size: 9.5px; }
  .tagline-sub { fill: var(--navy); font-weight: 600; font-size: 9.5px; }
</style>
</head>
<body>
<svg class="livery" viewBox="0 0 1652 2265" xmlns="http://www.w3.org/2000/svg" aria-label="vELRA Linehaul trailer livery: rear view, left side, right side">
  <defs>
    <g id="tick-mark"><path class="tick" d="M0 6 L5 11 L14 0"/></g>
  </defs>

  <!-- Rear view -->
  <g class="rear-view">
    <rect class="white-fill" x="500" y="82" width="640" height="583"/>
    <text class="brand-name" x="572" y="250" font-size="180" textLength="440" lengthAdjust="spacingAndGlyphs">velra</text>
    <circle class="brand-dot" cx="1040" cy="232" r="18"/>
    <text class="linehaul-tag" x="574" y="306" font-size="34" textLength="436" lengthAdjust="spacing">LINEHAUL</text>
    <path class="flight-path on-white" d="M560 500 Q800 340 1080 392"/>
    <circle class="flight-end" cx="1086" cy="393" r="7"/>
    <rect class="navy-fill" x="500" y="545" width="640" height="120"/>
    <line x1="500" y1="545" x2="1140" y2="545" stroke="var(--red)" stroke-width="5"/>
    <rect class="panel-frame" x="500" y="82" width="640" height="583"/>
  </g>

  <!-- Left side view -->
  <g class="left-side">
    <rect class="white-fill" x="90" y="1195" width="1460" height="287"/>
    <polygon class="navy-fill" points="90,1195 652,1195 800,1345 666,1482 90,1482"/>
    <polyline class="red-edge" points="652,1195 802,1345 668,1482"/>
    <path class="flight-path on-navy" d="M105 1460 Q170 1240 420 1218"/>
    <circle class="flight-end" cx="426" cy="1218" r="7"/>

    <text class="services-title" x="508" y="1270">Szolgáltatások:</text>
    <g class="service-list">
      <use href="#tick-mark" x="478" y="1284"/><text class="service-item" x="493" y="1297">. TENGERI SZÁLLÍTÁS</text>
      <use href="#tick-mark" x="478" y="1304"/><text class="service-item" x="493" y="1317">. LÉGI SZÁLLÍTÁS</text>
      <use href="#tick-mark" x="478" y="1324"/><text class="service-item" x="493" y="1337">. ESŐVÍZ SZÁLLÍTÁS</text>
      <use href="#tick-mark" x="478" y="1344"/><text class="service-item" x="493" y="1357">. ALVÁZ SZÁLLÍTÁS</text>
      <use href="#tick-mark" x="478" y="1364"/><text class="service-item" x="493" y="1377">. ENGEDÉLYEK</text>
    </g>
    <text class="phone" x="358" y="1436">+36 70 555 0148</text>
    <text class="web" x="365" y="1462">www.velrafreight.com</text>

    <text class="brand-name" x="870" y="1390" font-size="220" textLength="560" lengthAdjust="spacingAndGlyphs">velra</text>
    <circle class="brand-dot" cx="1462" cy="1370" r="20"/>
    <text class="linehaul-tag" x="874" y="1428" font-size="26" textLength="556" lengthAdjust="spacing">LINEHAUL</text>

    <text class="tagline" x="1180" y="1455" text-anchor="middle">NE VÁRJON NAPOKAT EGY AJÁNLATRA, HASONLÍTSA ÖSSZE MOST A HAJTÓTÁRSASÁGOK ÁLTAL KÍNÁLT SZOLGÁLTATÁSOKAT ÉS ÁRAKAT!</text>
    <text class="tagline-sub" x="1180" y="1468" text-anchor="middle">Nézze meg, válassza ki, és foglalja le a legközelebb induló hajót „MI”-támogatott rendszerünk segítségével!</text>
    <rect class="panel-frame" x="90" y="1195" width="1460" height="287"/>
  </g>

  <!-- Right side view -->
  <g class="right-side">
    <rect class="white-fill" x="100" y="1777" width="1460" height="286"/>
    <polygon class="navy-fill" points="998,1777 1560,1777 1560,2063 986,2063 850,1928"/>
    <polyline class="red-edge" points="996,1777 846,1928 984,2063"/>
    <path class="flight-path on-navy" d="M1540 2045 Q1490 1820 1240 1800"/>
    <circle class="flight-end" cx="1234" cy="1800" r="7"/>

    <text class="brand-name" x="150" y="1972" font-size="220" textLength="560" lengthAdjust="spacingAndGlyphs">velra</text>
    <circle class="brand-dot" cx="742" cy="1952" r="20"/>
    <text class="linehaul-tag" x="154" y="2010" font-size="26" textLength="556" lengthAdjust="spacing">LINEHAUL</text>

    <text class="tagline" x="470" y="2036" text-anchor="middle">NE VÁRJON NAPOKAT EGY AJÁNLATRA, HASONLÍTSA ÖSSZE MOST A HAJTÓTÁRSASÁGOK ÁLTAL KÍNÁLT SZOLGÁLTATÁSOKAT ÉS ÁRAKAT!</text>
    <text class="tagline-sub" x="470" y="2049" text-anchor="middle">Nézze meg, válassza ki, és foglalja le a legközelebb induló hajót „MI”-támogatott rendszerünk segítségével!</text>

    <text class="services-title" x="1008" y="1852">Szolgáltatások:</text>
    <g class="service-list">
      <use href="#tick-mark" x="978" y="1866"/><text class="service-item" x="993" y="1879">. TENGERI SZÁLLÍTÁS</text>
      <use href="#tick-mark" x="978" y="1886"/><text class="service-item" x="993" y="1899">. LÉGI SZÁLLÍTÁS</text>
      <use href="#tick-mark" x="978" y="1906"/><text class="service-item" x="993" y="1919">. ESŐVÍZ SZÁLLÍTÁS</text>
      <use href="#tick-mark" x="978" y="1926"/><text class="service-item" x="993" y="1939">. ALVÁZ SZÁLLÍTÁS</text>
      <use href="#tick-mark" x="978" y="1946"/><text class="service-item" x="993" y="1959">. ENGEDÉLYEK</text>
    </g>
    <text class="phone" x="1012" y="2016">+36 70 555 0148</text>
    <text class="web" x="1019" y="2043">www.velrafreight.com</text>
    <rect class="panel-frame" x="100" y="1777" width="1460" height="286"/>
  </g>
</svg>
</body>
</html>
```